Need a fresh corporate identity for an existing Home Shopping Business in Thailand

We are one of the most active TV home shopping companies in Thailand. We need a fresh looking CI for our corporate, the colours of our corporate are Orange and Grey. We want our customers to see us as professional customer service who help them with their purchases.
The logo can be shown as a whole logo or either half logo but not less than half the logo.
Industry/Entity Type
Shopping
Requirements
Must have
- The logo should be shown at least half the logo or full logo.
Should not have
- The logo should not be shown less than half the logo.

```html
<!DOCTYPE html>
<html lang="en">
<head>
<meta charset="utf-8">
<title>Lumora Stationery Identity</title>
<link href="https://fonts.googleapis.com/css2?family=Source+Sans+3:wght@400;600&display=swap" rel="stylesheet">
<style>
  :root{
    --bg:#bfc0c2;
    --paper:#f1f1f1;
    --folder:#d9dadb;
    --orange:#d2662c;
    --peach:#d4a186;
    --ink:#6b6b6b;
    --flap:#e4e4e4;
    --fold:#cfcfcf;
  }
  *{margin:0;padding:0;box-sizing:border-box}
  html,body{width:1200px;height:1000px;overflow:hidden}
  body{background:var(--bg);font-family:"Source Sans 3",Arial,sans-serif;position:relative}
  .piece{position:absolute;overflow:hidden}
  .brand{position:absolute;display:flex;flex-direction:column;align-items:center;transform:translateX(-50%)}
  .brand-mark{background:var(--orange)}
  .brand-name{font-weight:400;color:var(--orange);white-space:nowrap;line-height:1}

  .folder{left:84px;top:267px;width:340px;height:458px;background:var(--folder)}
  .folder .brand{left:50%;top:66px}
  .folder .brand-mark{width:46px;height:46px}
  .folder .brand-name{font-size:12px;margin-top:8px}
  .folder-block{position:absolute;left:12px;top:294px;width:316px;height:164px;background:var(--peach)}

  .letterhead{left:452px;top:282px;width:313px;height:441px;background:var(--paper)}
  .letterhead .brand{left:50%;top:20px}
  .letterhead .brand-mark{width:32px;height:32px}
  .letterhead .brand-name{font-size:7px;margin-top:5px}

  .footer{position:absolute;border-top:1px solid var(--orange);padding-top:4px;display:flex;font-size:4px;color:var(--ink);line-height:1.6;white-space:nowrap}
  .footer .company{flex:1}
  .footer .company strong{display:block;font-size:5.5px;font-weight:600;color:var(--orange);line-height:1.3}
  .footer .col{width:62px;padding-top:7px}
  .letterhead .footer{top:396px;left:22px;right:22px}

  .card{top:256px;width:126px;height:82px;background:var(--paper)}
  .card-front{left:811px}
  .card-front .brand{left:50%;top:26px}
  .card-front .brand-mark{width:20px;height:20px}
  .card-front .brand-name{font-size:4.5px;margin-top:3px}
  .card-back{left:990px}
  .card-back-block{position:absolute;left:0;top:0;width:30px;height:82px;background:var(--peach)}
  .card-details{position:absolute;right:6px;top:22px;text-align:right;color:var(--ink);font-size:3.6px;line-height:1.5;white-space:nowrap}
  .card-details .person{position:absolute;right:0;top:-22px;font-size:7.5px;color:var(--orange);line-height:1.1}
  .card-details .role{position:absolute;right:0;top:-12px;font-size:4.8px}

  .envelope-front{left:798px;top:363px;width:328px;height:164px;background:var(--paper)}
  .envelope-front .brand{left:38px;top:14px}
  .envelope-front .brand-mark{width:24px;height:24px}
  .envelope-front .brand-name{font-size:5px;margin-top:3px}
  .envelope-front .footer{top:131px;left:20px;right:108px}
  .envelope-front .footer .col{width:42px}

  .envelope-back{left:800px;top:555px;width:328px;height:163px;background:var(--paper)}
  .envelope-flap{position:absolute;left:0;top:0}
  .envelope-back .brand{left:50%;top:16px}
  .envelope-back .brand-mark{width:22px;height:22px}
  .envelope-back .brand-name{font-size:4.5px;margin-top:3px}
</style>
</head>
<body>

<section class="piece folder">
  <div class="brand"><span class="brand-mark"></span><span class="brand-name">Lumora</span></div>
  <div class="folder-block" role="img" aria-label="Large soft peach brand shape rising from the lower edge"></div>
</section>

<section class="piece letterhead">
  <div class="brand"><span class="brand-mark"></span><span class="brand-name">Lumora</span></div>
  <div class="footer">
    <div class="company"><strong>Harbor Lane Co., Ltd.</strong>Company No. 0105 Meridian Court, 2nd Floor,<br>Soi Maple 7, Lantern Rd., Riverside, Bangkok 10990</div>
    <div class="col">T: 02-000-1234<br>F: 02-000-1235</div>
    <div class="col">E: hello@lumora.co<br>W: www.lumora.co</div>
  </div>
</section>

<section class="piece card card-front">
  <div class="brand"><span class="brand-mark"></span><span class="brand-name">Lumora</span></div>
</section>

<section class="piece card card-back">
  <div class="card-back-block" role="img" aria-label="Peach brand shape along the left edge"></div>
  <div class="card-details">
    <div class="person">Daniel Reyes</div>
    <div class="role">Managing Partner</div>
    <br>Lantern Rd., Riverside,<br>Bangkok 10990<br>T: 02-000-1234<br>E: daniel@lumora.co<br>W: www.lumora.co
  </div>
</section>

<section class="piece envelope-front">
  <div class="brand"><span class="brand-mark"></span><span class="brand-name">Lumora</span></div>
  <div class="footer">
    <div class="company"><strong>Harbor Lane Co., Ltd.</strong>Company No. 0105 Meridian Court, 2nd Floor,<br>Soi Maple 7, Lantern Rd., Riverside, Bangkok 10990</div>
    <div class="col">T: 02-000-1234<br>F: 02-000-1235</div>
    <div class="col">E: hello@lumora.co<br>W: www.lumora.co</div>
  </div>
</section>

<section class="piece envelope-back">
  <svg class="envelope-flap" width="328" height="163" viewBox="0 0 328 163">
    <polygon points="0,0 328,0 328,36 318,62 10,62 0,36" fill="var(--flap)"/>
    <line x1="0" y1="63" x2="328" y2="63" stroke="var(--fold)" stroke-width="1"/>
  </svg>
  <div class="brand"><span class="brand-mark"></span><span class="brand-name">Lumora</span></div>
</section>

</body>
</html>
```